We're a SEA Media Company that needs a fresh new look for one of our SG sites.

the site targets those that are researching apartment or home renovations and who want to get ideas and inspiration. the site is supported by a significant print magazine that is bi monthly. the attached design needs less grid and clutter.

the audience generally want to see designers and products they can use.

currently the site is zintaremura.com.sg.

```html
<!DOCTYPE html>
<html lang="en">
<head>
<meta charset="utf-8">
<title>Zintaremura – Home</title>
<link rel="stylesheet" href="https://fonts.googleapis.com/css2?family=Open+Sans:wght@400;600&family=Roboto:wght@400;500;700&display=swap">
<style>
  :root {
    --blue: #0aa0d8;
    --ink: #111111;
    --text: #333333;
    --orange: #e08a1e;
    --grey-band: #efefef;
    --caption: #474747;
    --footer: #1b1b1b;
    --white: #ffffff;
    --line: #d6d6d6;
  }
  * { box-sizing: border-box; margin: 0; padding: 0; }
  html, body { width: 671px; height: 1200px; overflow: hidden; background: var(--white); }
  body { position: relative; font-family: "Open Sans", Arial, sans-serif; color: var(--text); }
  .abs { position: absolute; }

  .top-rule { left: 0; top: 0; width: 671px; height: 2px; background: #555; }
  .brand { left: 101px; top: 22px; font-family: "Roboto", Arial, sans-serif; font-weight: 400; font-size: 25px; color: var(--blue); letter-spacing: -0.3px; }
  .search { left: 415px; top: 28px; width: 155px; height: 27px; border: 1px solid #cfcfcf; background: var(--white); display: flex; align-items: center; justify-content: space-between; padding: 0 8px; font-size: 6.5px; color: #999; }

  .nav { left: 0; top: 73px; width: 671px; height: 30px; background: var(--blue); }
  .nav-base { left: 0; top: 103px; width: 671px; height: 4px; background: var(--ink); }
  .nav-item { top: 73px; height: 30px; line-height: 30px; font-family: "Roboto", Arial, sans-serif; font-size: 7.2px; color: var(--white); transform: translateX(-50%); white-space: nowrap; }
  .nav-item.is-active { background: var(--ink); width: 40px; text-align: center; }
  .social { top: 80.5px; width: 15px; height: 15px; border-radius: 50%; background: var(--white); }

  .hero { left: 0; top: 107px; width: 671px; height: 308px;
    background: linear-gradient(90deg, #8c8a80 0%, #d9d6cf 20%, #ecebe8 42%, #c9cdcf 58%, #7fc2bc 72%, #c9e0dc 86%, #9aa7a5 100%); }
  .hero-floor { left: 0; top: 300px; width: 671px; height: 115px; background: linear-gradient(180deg, rgba(230,226,220,0) 0%, rgba(215,210,204,0.8) 100%); }
  .hero-rule { left: 0; top: 415px; width: 671px; height: 1px; background: var(--blue); }
  .hero-caption { left: 102px; top: 301px; width: 234px; height: 57px; background: rgba(40,40,40,0.82); color: var(--white); font-weight: 600; font-size: 11.6px; line-height: 23px; padding: 5px 0 0 13px; }
  .hero-arrow { top: 254px; }
  .dot { width: 6px; height: 6px; border-radius: 50%; transform: translate(-50%, -50%); }
  .dot.hollow { background: var(--white); }
  .dot.hollow.current { background: transparent; border: 1.5px solid var(--white); }

  .section-title { left: 0; width: 671px; text-align: center; font-family: "Roboto", Arial, sans-serif; font-size: 11.5px; color: var(--blue); }
  .welcome-text { left: 98px; top: 452px; width: 475px; text-align: center; font-size: 6.3px; line-height: 12px; color: var(--text); }
  .btn { background: var(--blue); color: var(--white); font-family: "Roboto", Arial, sans-serif; font-size: 6.8px; text-align: center; }

  .featured { left: 0; top: 523px; width: 671px; height: 206px; background: var(--grey-band); }
  .featured-photo { left: 101px; top: 571px; width: 218px; height: 135px; background: linear-gradient(135deg, #6f8cae 0%, #b9c3cc 40%, #e7e3dc 60%, #8a6a4c 100%); }
  .project-title { left: 332px; top: 574px; font-family: "Roboto", Arial, sans-serif; font-size: 8.3px; color: var(--orange); }
  .project-text { left: 332px; top: 591px; width: 236px; font-size: 6.2px; line-height: 11.5px; color: var(--text); }
  .project-meta { left: 335px; font-size: 6px; font-weight: 600; color: var(--ink); }
  .side-arrow { top: 633px; }

  .designer-card { top: 769px; width: 110px; }
  .designer-photo { height: 85px; }
  .designer-name { height: 28px; line-height: 28px; background: var(--caption); color: var(--white); font-size: 6.4px; padding-left: 10px; }

  .events { left: 101px; top: 924px; width: 310px; height: 137px; background: var(--blue); color: var(--white); }
  .panel-title { font-family: "Roboto", Arial, sans-serif; font-size: 8.2px; }
  .event { top: 32px; width: 92px; }
  .event-photo { height: 58px; border: 1px solid var(--white); }
  .event-title { margin-top: 6px; font-family: "Roboto", Arial, sans-serif; font-size: 7.3px; }
  .event-text { margin-top: 3px; font-size: 5.4px; line-height: 8px; }

  .magazine { left: 420px; top: 924px; width: 151px; height: 137px; background: var(--grey-band); border: 1px solid var(--line); }
  .magazine-head { left: -1px; top: -1px; width: 151px; height: 31px; background: var(--caption); color: var(--white); padding: 10px 11px; }
  .magazine-cover { left: 18px; top: 39px; width: 115px; height: 72px; background: linear-gradient(160deg, #ffffff 0%, #f1f1f1 40%, #4a8fc9 75%, #e9d64a 100%); }
  .read-more { right: 17px; top: 119px; font-size: 6.3px; color: var(--orange); }

  .footer { left: 0; top: 1087px; width: 671px; height: 113px; background: var(--footer); color: var(--white); }
  .newsletter-title { left: 0; top: 14px; width: 671px; text-align: center; font-family: "Roboto", Arial, sans-serif; font-size: 8.4px; }
  .email { left: 200px; top: 35px; width: 187px; height: 22px; background: #ececec; color: #555; font-family: "Roboto", Arial, sans-serif; font-size: 6.3px; line-height: 22px; padding-left: 8px; }
  .subscribe { left: 397px; top: 35px; width: 75px; height: 22px; line-height: 22px; font-size: 8px; font-weight: 500; }
  .footer-rule { left: 101px; top: 75px; width: 470px; height: 1px; background: #333; }
  .footer-links, .copyright { top: 89px; font-family: "Roboto", Arial, sans-serif; font-size: 5.3px; font-weight: 500; letter-spacing: 0.1px; }
  .footer-links { left: 102px; }
  .copyright { right: 101px; }
</style>
</head>
<body>

<div class="abs top-rule"></div>
<header>
  <div class="abs brand">zintaremura.com.sg</div>
  <div class="abs search">
    <span>Search...</span>
    <svg width="9" height="9" viewBox="0 0 10 10"><circle cx="4.2" cy="4.2" r="3" fill="none" stroke="#999" stroke-width="1.4"/><line x1="6.4" y1="6.4" x2="9" y2="9" stroke="#999" stroke-width="1.6"/></svg>
  </div>
</header>

<nav>
  <div class="abs nav"></div>
  <div class="abs nav-base"></div>
  <div class="abs nav-item is-active" style="left:116px">Home</div>
  <div class="abs nav-item" style="left:162px">Designers</div>
  <div class="abs nav-item" style="left:212px">Projects</div>
  <div class="abs nav-item" style="left:259px">Products</div>
  <div class="abs nav-item" style="left:309px">Directory</div>
  <div class="abs nav-item" style="left:353px">News</div>
  <div class="abs nav-item" style="left:393px">Events</div>
  <div class="abs nav-item" style="left:441px">Contact Us</div>
  <div class="abs social" style="left:489px"></div>
  <div class="abs social" style="left:506px"></div>
  <div class="abs social" style="left:523px"></div>
  <div class="abs social" style="left:539px"></div>
  <div class="abs social" style="left:556px"></div>
</nav>

<section>
  <div class="abs hero" role="img" aria-label="Bright modern living and dining room with white sofa, teal glass wall and red chairs"></div>
  <div class="abs hero-floor"></div>
  <div class="abs hero-rule"></div>
  <div class="abs hero-caption">Quisque ligulas ipsum, euismod atras<br>vulputate iltricies etri elit.</div>
  <svg class="abs hero-arrow" style="left:10px" width="18" height="18" viewBox="0 0 18 18"><circle cx="9" cy="9" r="8" fill="#fff" stroke="#888" stroke-width="1"/><path d="M10.5 5.5 L7 9 L10.5 12.5" fill="none" stroke="#777" stroke-width="1.6"/></svg>
  <svg class="abs hero-arrow" style="left:638px" width="18" height="18" viewBox="0 0 18 18"><circle cx="9" cy="9" r="8" fill="#fff" stroke="#888" stroke-width="1"/><path d="M7.5 5.5 L11 9 L7.5 12.5" fill="none" stroke="#777" stroke-width="1.6"/></svg>
  <div class="abs dot hollow" style="left:318px; top:398px"></div>
  <div class="abs dot hollow current" style="left:335px; top:398px"></div>
  <div class="abs dot hollow" style="left:354px; top:398px"></div>
</section>

<section>
  <h2 class="abs section-title" style="top:432px">Welcome To Zintaremura</h2>
  <p class="abs welcome-text">Lorem ipsum dolor sit amet, consectetuer adipiscing elit, sed diam nonummy nibh euismod tincidunt ut laoreet dolore magna aliquam erat volutpat. Ut wisi enim ad minim veniam, quis nostrud exerci tation ullamcorper suscipit lobortis nisl ut aliquip ex ea commodo consequat.</p>
  <div class="abs btn" style="left:303px; top:483px; width:63px; height:19px; line-height:19px">Read More</div>
</section>

<section>
  <div class="abs featured"></div>
  <h2 class="abs section-title" style="top:540px">Featured Projects</h2>
  <div class="abs featured-photo" role="img" aria-label="Bedroom with blue wall, patterned bedspread and white wardrobe"></div>
  <h3 class="abs project-title">Blocks of Colour</h3>
  <p class="abs project-text">This three-storey inter-terrace house is home to a well-travelled family. Having been exposed to different global influences naturally led to a home that comfor balances different styles without looking like a hodgepodge mess. Ceravel designers came up with a plan to turn this 4,000-sqft house into an international home. Instead of bringing in overpowering design elements....</p>
  <div class="abs project-meta" style="top:657px">Designer</div>
  <div class="abs project-meta" style="top:669px">The Amber Frame</div>
  <div class="abs btn" style="left:332px; top:685px; width:62px; height:21px; line-height:21px">View Details</div>
  <svg class="abs side-arrow" style="left:7px" width="16" height="16" viewBox="0 0 16 16"><circle cx="8" cy="8" r="8" fill="#a9a9a9"/><path d="M9.5 4.5 L6 8 L9.5 11.5" fill="none" stroke="#fff" stroke-width="1.6"/></svg>
  <svg class="abs side-arrow" style="left:648px" width="16" height="16" viewBox="0 0 16 16"><circle cx="8" cy="8" r="8" fill="#a9a9a9"/><path d="M6.5 4.5 L10 8 L6.5 11.5" fill="none" stroke="#fff" stroke-width="1.6"/></svg>
</section>

<section>
  <h2 class="abs section-title" style="top:746px">Our Designers</h2>
  <div class="abs designer-card" style="left:101px">
    <div class="designer-photo" role="img" aria-label="Portrait of a design duo" style="background:linear-gradient(90deg,#c5d33a 0%,#8c9a3a 35%,#2a2a2a 60%,#dcdcdc 100%)"></div>
    <div class="designer-name">Lorem ipsum dolor</div>
  </div>
  <div class="abs designer-card" style="left:221px">
    <div class="designer-photo" role="img" aria-label="Portrait of two designers" style="background:linear-gradient(90deg,#f1f1f1 0%,#dedede 50%,#f3f3f3 100%)"></div>
    <div class="designer-name">Duis autem vel eum iriure</div>
  </div>
  <div class="abs designer-card" style="left:341px">
    <div class="designer-photo" role="img" aria-label="Portrait of a three-person design team" style="background:linear-gradient(90deg,#f2f2f2 0%,#4a6fa8 30%,#d8dde3 55%,#2f3540 80%,#f2f2f2 100%)"></div>
    <div class="designer-name">Nam liber tempor cum</div>
  </div>
  <div class="abs designer-card" style="left:461px">
    <div class="designer-photo" role="img" aria-label="Portrait of two designers in a studio" style="background:linear-gradient(90deg,#c5d33a 0%,#e9e6dc 40%,#3d3f45 75%,#dedede 100%)"></div>
    <div class="designer-name">Typi non habent claritatem</div>
  </div>
  <div class="abs dot" style="left:321px; top:902px; background:var(--blue)"></div>
  <div class="abs dot" style="left:335px; top:902px; background:var(--orange)"></div>
  <div class="abs dot" style="left:350px; top:902px; background:var(--blue)"></div>
</section>

<section class="abs events">
  <h3 class="abs panel-title" style="left:12px; top:12px">Events</h3>
  <article class="abs event" style="left:9px">
    <div class="event-photo" role="img" aria-label="Purple-toned bedroom" style="background:linear-gradient(135deg,#5b3f62,#cbb6cf 55%,#f0ecee)"></div>
    <div class="event-title">Mauris interdum</div>
    <div class="event-text">Mauris interdum imperdiet lorem vitae placerat.</div>
  </article>
  <article class="abs event" style="left:108px">
    <div class="event-photo" role="img" aria-label="Warm wood-panelled lounge" style="background:linear-gradient(135deg,#6b3f1c,#d39a5a 50%,#f1dcb8)"></div>
    <div class="event-title">Ut wisi enim ad</div>
    <div class="event-text">Mauris interdum imperdiet lorem vitae placerat.</div>
  </article>
  <article class="abs event" style="left:206px">
    <div class="event-photo" role="img" aria-label="Black and white living room" style="background:linear-gradient(135deg,#2b2b2b,#9a9a9a 50%,#f2f2f2)"></div>
    <div class="event-title">Mauris interdum</div>
    <div class="event-text">Mauris interdum imperdiet lorem vitae placerat.</div>
  </article>
</section>

<aside class="abs magazine">
  <h3 class="abs magazine-head panel-title">Our Magazine</h3>
  <div class="abs magazine-cover" role="img" aria-label="Current print magazine cover with bright interior"></div>
  <div class="abs read-more">Read More</div>
</aside>

<footer class="abs footer">
  <h3 class="abs newsletter-title">Newsletter Signup</h3>
  <div class="abs email">Enter Your Email Address</div>
  <div class="abs btn subscribe">Subscribe</div>
  <div class="abs footer-rule"></div>
  <div class="abs footer-links">TERMS &amp; CONDITIONS &nbsp;| &nbsp;PRIVACY NOTICE &nbsp;| &nbsp;SITEMAP &nbsp;| &nbsp;FAQ &nbsp;| &nbsp;CONTACT</div>
  <div class="abs copyright">COPYRIGHT © 2014 ZINTAREMURA. ALL RIGHTS RESERVED.</div>
</footer>

</body>
</html>
```